Job advert for Forged Here Collective

I would like a poster graphic that I can promote on social media to advertise a job vacancy we will be promoting our upcoming jobs, here is the text...

WE ARE ON THE…

LOOKOUT
(maybe insert graphic or icon that fits with the message here)

For A

OPERATIONS AND HR MANAGER

MEMBERSHIP ADVISOR (EAST MIDLANDS)

SOCIAL MEDIA CONTENT CREATOR

THE UK’s FASTEST GROWING NETWORK FOR MANUFACTURERS

OFFICES IN BIRMINGHAM AND LEEDS - WE ARE AN INCLUSIVE EMPLOYER (use the equality logo provided here)

Target Market(s)

people looking to find a new job

Industry/Entity Type

Manufacture

Font styles to use
Sans Serif

Colors
f04a50
f68e4e
e667a6

Requirements
Must have
• Clear simple and contemporary style
Nice to have
• a nice graphic or icon to convey the text message
Should not have
• use of dark depressing colours

```html
<!DOCTYPE html>
<html lang="en">
<head>
<meta charset="utf-8">
<title>Forged Here Collective – Job Vacancies</title>
<link href="https://fonts.googleapis.com/css2?family=Montserrat:wght@800&family=Roboto+Condensed:ital,wght@1,700&family=Arimo:wght@400;700&display=swap" rel="stylesheet">
<style>
  :root {
    --orange: #f68e4e;
    --red: #f04a50;
    --magenta: #e0119a;
    --pink: #e667a6;
    --purple: #8c2a91;
    --deep-purple: #7a2483;
    --grey: #e2e2e2;
    --ink: #2b2b2b;
    --white: #ffffff;
    --green: #9cc63b;
    --photo-dark: #0f1a33;
    --photo-light: #aeb7c6;
  }
  * { margin: 0; padding: 0; box-sizing: border-box; }
  html, body { width: 1200px; height: 798px; overflow: hidden; background: var(--white); }
  .poster { position: relative; width: 1200px; height: 798px; overflow: hidden; background: var(--white); font-family: "Arimo", Arial, sans-serif; }

  .headline-panel { position: absolute; left: 0; top: 0; width: 560px; height: 470px; background: var(--orange); }
  .pledge { position: absolute; left: 40px; top: 36px; display: flex; align-items: center; gap: 14px; }
  .pledge-mark { width: 70px; height: 70px; border-radius: 50%; background: var(--purple); }
  .pledge-name { font-family: "Arimo", sans-serif; font-weight: 400; font-size: 24px; line-height: 1; color: var(--white); }
  .headline { position: absolute; left: 40px; top: 140px; font-family: "Montserrat", sans-serif; font-weight: 800; line-height: 0.98; color: var(--white); text-transform: uppercase; }
  .headline .line { display: block; font-size: 58px; letter-spacing: -1px; }
  .headline .looking { font-size: 82px; letter-spacing: 2px; }
  .headline .for-a { display: block; font-size: 64px; color: #3a3a3a; text-transform: none; }

  .top-band { position: absolute; left: 560px; top: 0; width: 640px; height: 58px; background: var(--purple); }
  .photo { position: absolute; left: 578px; top: 72px; width: 622px; height: 372px;
    background: radial-gradient(circle at 70% 55%, #f5c16a 0 4%, transparent 14%), linear-gradient(120deg, var(--photo-light) 0%, #5b6a86 38%, #1d2a4a 65%, var(--photo-dark) 100%); }
  .accent-strip { position: absolute; left: 578px; top: 444px; width: 622px; height: 26px; background: var(--red); }

  .jobs { position: absolute; left: 0; top: 470px; width: 1200px; height: 104px; background: var(--grey); display: flex; align-items: center; padding: 0 30px; }
  .job { display: flex; align-items: center; gap: 16px; padding: 0 34px; border-left: 3px solid var(--red); height: 70px; }
  .job:last-child { border-right: 3px solid var(--red); }
  .job svg { flex: none; }
  .job-title { font-size: 22px; line-height: 1.15; color: var(--ink); text-transform: uppercase; letter-spacing: 0.5px; }

  .tagline { position: absolute; left: 0; top: 574px; width: 1200px; height: 66px; background: var(--white); display: flex; align-items: center; padding-left: 40px; white-space: nowrap;
    font-family: "Roboto Condensed", sans-serif; font-style: italic; font-weight: 700; font-size: 40px; line-height: 1; color: var(--deep-purple); text-transform: uppercase; letter-spacing: 0.3px; }

  .footer { position: absolute; left: 0; top: 640px; width: 1200px; height: 158px; }
  .footer-band { position: absolute; inset: 0; }
  .partners { position: absolute; left: 36px; top: 28px; display: flex; flex-direction: column; gap: 20px; }
  .partner { display: flex; align-items: center; gap: 10px; font-family: "Arimo", sans-serif; font-weight: 700; font-size: 17px; text-transform: uppercase; }
  .partner .mark { width: 34px; height: 34px; border-radius: 50%; }
  .partner.yorkshire { color: var(--green); }
  .partner.yorkshire .mark { background: var(--green); }
  .partner.midlands { color: var(--red); }
  .partner.midlands .mark { background: var(--red); }
  .offices { position: absolute; left: 420px; top: 30px; width: 680px; text-align: center; color: var(--white); font-size: 24px; line-height: 1.4; text-transform: uppercase; letter-spacing: 0.5px; }
</style>
</head>
<body>
<main class="poster">
  <section class="headline-panel">
    <div class="pledge">
      <span class="pledge-mark" aria-hidden="true"></span>
      <span class="pledge-name">open to all<br>pledge</span>
    </div>
    <h1 class="headline">
      <span class="line">We are</span>
      <span class="line">on the…</span>
      <span class="line looking">Looking</span>
      <span class="for-a">For A</span>
    </h1>
  </section>

  <div class="top-band"></div>
  <div class="photo" role="img" aria-label="Photograph of a hand touching a glowing network of small human figures on a blue business background"></div>
  <div class="accent-strip"></div>

  <section class="jobs">
    <div class="job">
      <svg width="46" height="46" viewBox="0 0 46 46" aria-hidden="true">
        <rect x="4" y="14" width="38" height="26" rx="3" fill="#1f1f1f"/>
        <rect x="16" y="7" width="14" height="9" rx="2" fill="none" stroke="#1f1f1f" stroke-width="3"/>
        <rect x="4" y="24" width="38" height="3" fill="#2f7fd1"/>
      </svg>
      <p class="job-title">Operations<br>and HR Manager</p>
    </div>
    <div class="job">
      <svg width="50" height="46" viewBox="0 0 50 46" aria-hidden="true">
        <rect x="2" y="4" width="26" height="18" rx="3" fill="#1f1f1f"/>
        <path d="M8 22 L8 29 L15 22Z" fill="#1f1f1f"/>
        <rect x="22" y="18" width="26" height="18" rx="3" fill="#2f7fd1"/>
        <path d="M42 36 L42 43 L35 36Z" fill="#2f7fd1"/>
      </svg>
      <p class="job-title">Membership Advisor<br>(East Midlands)</p>
    </div>
    <div class="job">
      <svg width="50" height="46" viewBox="0 0 50 46" aria-hidden="true">
        <rect x="9" y="8" width="32" height="22" rx="2" fill="#1f1f1f"/>
        <rect x="12" y="11" width="26" height="16" fill="#2f7fd1"/>
        <path d="M3 34 H47 L43 40 H7Z" fill="#1f1f1f"/>
      </svg>
      <p class="job-title">Social Media<br>Content Creator</p>
    </div>
  </section>

  <h2 class="tagline">The UK’s fastest growing network for manufacturers</h2>

  <footer class="footer">
    <svg class="footer-band" width="1200" height="158" viewBox="0 0 1200 158" aria-hidden="true">
      <polygon points="380,0 1200,0 1200,158 300,158" fill="var(--magenta)"/>
      <polygon points="1080,60 1200,60 1200,158 990,158" fill="var(--red)"/>
    </svg>
    <div class="partners">
      <div class="partner yorkshire"><span class="mark"></span>Forged Here Yorkshire</div>
      <div class="partner midlands"><span class="mark"></span>Forged Here Midlands</div>
    </div>
    <p class="offices">Offices in Birmingham and Leeds – we are an<br>inclusive employer</p>
  </footer>
</main>
</body>
</html>
```